New letter head for Air Conditioning business

We need a new professional letter head design to suit our new re-branded air conditioning business. Our new logo is attached

```html
<!DOCTYPE html>
<html lang="en">
<head>
<meta charset="utf-8">
<title>Norvale Letterhead</title>
<link href="https://fonts.googleapis.com/css2?family=Montserrat:ital,wght@0,400;0,500;0,600;0,700;1,400&display=swap" rel="stylesheet">
<style>
  :root {
    --ink: #3a3a3a;
    --text: #2f2f2f;
    --paper: #ffffff;
    --backdrop: #ffffff;
    --band: #3a3a3a;
    --brand-green: #6cc28c;
    --brand-coral: #ef6f5e;
    --on-band: #ffffff;
  }
  * { margin: 0; padding: 0; box-sizing: border-box; }
  html, body {
    width: 1000px; height: 1200px; overflow: hidden;
    background: var(--backdrop);
    font-family: "Montserrat", Arial, sans-serif;
    color: var(--text);
  }
  .canvas { position: relative; width: 1000px; height: 1200px; }
  .letterhead {
    position: absolute; left: 117px; top: 58px; width: 766px; height: 1084px;
    background: var(--paper);
    box-shadow: 0 4px 18px rgba(0,0,0,0.12);
  }
  .brand {
    position: absolute; left: 248px; top: 40px; height: 72px;
    display: flex; align-items: center; gap: 16px;
  }
  .brand-dot { width: 46px; height: 46px; border-radius: 50%; background: var(--brand-green); }
  .brand-name {
    font-size: 36px; font-weight: 600; letter-spacing: 4px; color: var(--ink);
  }
  .letter-date {
    position: absolute; right: 112px; top: 245px;
    font-size: 13px; font-weight: 600; color: var(--ink);
  }
  .headline {
    position: absolute; left: 113px; top: 299px;
    font-size: 24px; font-weight: 700; letter-spacing: 1px; color: var(--ink);
  }
  .body-copy {
    position: absolute; left: 113px; width: 541px;
    font-size: 13px; line-height: 26px; letter-spacing: 0.55px;
    text-align: justify; text-align-last: left; color: var(--text);
  }
  .para-1 { top: 351px; }
  .para-2 { top: 533px; }
  .para-3 { top: 634px; }
  .signature {
    position: absolute; right: 118px; top: 780px; text-align: right; color: var(--ink);
  }
  .signature-name { font-size: 15px; font-weight: 700; letter-spacing: 0.6px; line-height: 20px; }
  .signature-role { font-size: 15px; font-style: italic; letter-spacing: 0.6px; line-height: 20px; }
  .signature-note { font-size: 11px; font-weight: 700; letter-spacing: 0.3px; line-height: 18px; }
  .footer-band {
    position: absolute; left: 0; top: 952px; width: 766px; height: 107px;
    background: var(--band); color: var(--on-band);
  }
  .contact-list { position: absolute; left: 46px; top: 23px; list-style: none; }
  .contact-list li {
    display: flex; align-items: center; gap: 6px;
    font-size: 13px; line-height: 22px; letter-spacing: 0.3px;
  }
  .contact-list svg { width: 11px; height: 11px; fill: var(--on-band); }
  .footer-brand {
    position: absolute; left: 0; width: 766px; top: 40px; text-align: center;
    font-size: 22px; font-weight: 600; letter-spacing: 4px;
  }
  .address { position: absolute; left: 526px; top: 30px; display: flex; gap: 9px; }
  .address svg { width: 14px; height: 16px; margin-top: 4px; fill: var(--on-band); }
  .address p { font-size: 13px; line-height: 22px; letter-spacing: 0.3px; }
</style>
</head>
<body>
<div class="canvas">
  <article class="letterhead">
    <header class="brand">
      <span class="brand-dot"></span>
      <span class="brand-name">NORVALE</span>
    </header>

    <p class="letter-date">Date: 06 June 2021</p>
    <h1 class="headline">Headline</h1>

    <p class="body-copy para-1">Lorem ipsum dolor sit amet, consectetur adipiscing elit. Fusce dignissim pretium consectetur. Curabitur tempor posuere massa in varius. Pellentesque viverra nibh eu vehicula mattis. Nullam porta facilisis justo, a feugiat dolor sodales sed. Vestibulum neque nisi, elementum tincidunt metus sit amet, egestas bibendum enim. Aenean a blandit elit, vel rutrum mi. Nunc dapibus turpis sed massa aliquet tincidunt.</p>
    <p class="body-copy para-2">Pellentesque id neque ligula. Nullam posuere, ligula a mattis posuere, lacus nisl adipiscing nunc, eu congue justo est ut diam. Nam quam nibh, dignissim non consequat in, semper eget purus. Nulla arcu sapien, viverra vitae metus tempor, congue ornare diam.</p>
    <p class="body-copy para-3">Pellentesque vel nibh tempus, ullamcorper tortor sed, bibendum augue. Phasellus sollicitudin justo et quam aliquam sollicitudin. Sed eget nibh mollis, mattis sem et, viverra nulla.</p>

    <div class="signature">
      <p class="signature-name">Your Name</p>
      <p class="signature-role">Designation</p>
      <p class="signature-note">Lorem ipsum dolor sit amet</p>
    </div>

    <footer class="footer-band">
      <ul class="contact-list">
        <li><svg viewBox="0 0 24 24"><path d="M6.6 10.8a15.1 15.1 0 0 0 6.6 6.6l2.2-2.2a1 1 0 0 1 1-.25 11.4 11.4 0 0 0 3.6.57 1 1 0 0 1 1 1V20a1 1 0 0 1-1 1A17 17 0 0 1 3 4a1 1 0 0 1 1-1h3.5a1 1 0 0 1 1 1c0 1.25.2 2.45.57 3.57a1 1 0 0 1-.25 1z"/></svg>+00 9876 5432 10</li>
        <li><svg viewBox="0 0 24 24"><path d="M2 5h20v14H2z M2 5l10 8 10-8" fill="none" stroke="#fff" stroke-width="2.5"/><path d="M2 5h20l-10 8z"/></svg>info@norvale.com</li>
        <li><svg viewBox="0 0 24 24"><path d="M5 2l14 12h-7l4 8-3 1.5-4-8-4 4z"/></svg>www.websitename.com</li>
      </ul>
      <p class="footer-brand">NORVALE</p>
      <div class="address">
        <svg viewBox="0 0 24 28"><path d="M12 0a10 10 0 0 0-10 10c0 7.5 10 18 10 18s10-10.5 10-18A10 10 0 0 0 12 0zm0 14.5A4.5 4.5 0 1 1 12 5.5a4.5 4.5 0 0 1 0 9z"/></svg>
        <p>3172&nbsp; Maren Ashford<br>Boulevard</p>
      </div>
    </footer>
  </article>
</div>
</body>
</html>
```